Vantor Medica Innovative Business Card

Stunning business card. Background will be black. Letters in gold. Modern yet simple design that is attention grabbing. QR code leading to site. Attractive primarily to males ages 30 to 50 but also to females in same age range looking for beauty and mental health products

Target Market(s)

Males in the 30-50 age demographics

Industry/Entity Type

Pharmaceuticals selling erectile dysfunction and mens health medications

Contact Information for Business Card

www.vantormedica.example; (640) BUY-KELO; info@vantormedica.example

Colors
FFC000
F8CF3A
FAE287
FDF2CF
FEFAEE

Requirements
Must have
• Black business card with gold letters.
Nice to have
• perhaps just the logo or the "R" icon by itself on one side
Should not have
• too much content so it does not look busy

```html
<!DOCTYPE html>
<html lang="en">
<head>
<meta charset="utf-8">
<title>Vantor Medica Business Card</title>
<link href="https://fonts.googleapis.com/css2?family=Montserrat:wght@400;500;600;700&display=swap" rel="stylesheet">
<style>
  :root {
    --stage: #111111;
    --card: #141414;
    --card-edge: #1d1d1d;
    --pattern-dark: #1a1a1a;
    --pattern-light: #262626;
    --gold: #c9961f;
    --gold-light: #e8b93a;
    --gold-soft: #fae287;
  }
  * { margin: 0; padding: 0; box-sizing: border-box; }
  html, body {
    width: 1200px; height: 900px; overflow: hidden;
    background: var(--stage);
    font-family: "Montserrat", sans-serif;
  }
  .canvas {
    position: relative; width: 1200px; height: 900px;
    background: radial-gradient(ellipse at 50% 40%, #1e1e1e 0%, var(--stage) 70%);
  }
  .card {
    position: absolute; left: 290px; width: 620px; height: 354px;
    background: var(--card);
    border: 1px solid var(--card-edge);
    box-shadow: 0 20px 40px rgba(0,0,0,0.6);
    overflow: hidden;
  }
  .card--back { top: 50px; }
  .card--front { top: 470px; }

  .back-pattern {
    position: absolute; inset: 0;
    background: linear-gradient(120deg, var(--pattern-light) 0%, var(--pattern-dark) 45%, var(--pattern-light) 100%);
  }
  .back-mark {
    position: absolute; right: 56px; bottom: 40px;
    display: flex; align-items: center; gap: 8px;
    color: var(--gold-light); font-weight: 700; font-size: 13px;
    letter-spacing: 0.04em; text-transform: uppercase;
  }
  .dot {
    width: 22px; height: 22px; border-radius: 50%;
    background: var(--gold-light);
  }

  .brand {
    position: absolute; right: 60px; top: 56px;
    display: flex; align-items: center; gap: 12px;
    color: var(--gold-light); font-weight: 700; font-size: 30px;
    letter-spacing: 0.02em; text-transform: uppercase;
  }
  .brand .dot { width: 34px; height: 34px; }

  .person { position: absolute; left: 44px; top: 170px; }
  .person__name {
    color: var(--gold-light); font-weight: 600; font-size: 24px;
    letter-spacing: 0.03em; text-transform: uppercase; line-height: 1.1;
  }
  .person__title {
    color: var(--gold-light); font-weight: 500; font-size: 14px;
    letter-spacing: 0.06em; text-transform: uppercase; margin-top: 2px;
  }
  .rule {
    position: absolute; left: 44px; right: 44px; top: 232px; height: 1px;
    background: var(--gold);
  }

  .contacts { position: absolute; left: 44px; top: 248px; list-style: none; }
  .contacts li {
    display: flex; align-items: center; gap: 8px;
    color: var(--gold-light); font-size: 15px; font-weight: 500; line-height: 24px;
  }
  .contacts svg { width: 11px; height: 11px; flex: none; }
</style>
</head>
<body>
<div class="canvas">

  <section class="card card--back">
    <div class="back-pattern" role="img" aria-label="Tonal repeating brand-mark pattern in dark grey"></div>
    <div class="back-mark"><span class="dot"></span>Vantor Medica</div>
  </section>

  <section class="card card--front">
    <div class="brand"><span class="dot"></span>Vantor Medica</div>

    <div class="person">
      <p class="person__name">Daniel Harlow</p>
      <p class="person__title">Director</p>
    </div>

    <div class="rule"></div>

    <ul class="contacts">
      <li>
        <svg viewBox="0 0 12 12" fill="none" stroke="#e8b93a" stroke-width="1.4"><path d="M3 1 L4.5 3.5 L3.5 4.5 Q5 7.5 7.5 8.5 L8.5 7.5 L11 9 L10 11 Q4 10.5 1 3 Z"/></svg>
        (640) BUY-KELO
      </li>
      <li>
        <svg viewBox="0 0 12 12" fill="none" stroke="#e8b93a" stroke-width="1.2"><rect x="1" y="2.5" width="10" height="7"/><path d="M1 2.5 L6 6.5 L11 2.5"/></svg>
        info@vantormedica.example
      </li>
      <li>
        <svg viewBox="0 0 12 12" fill="none" stroke="#e8b93a" stroke-width="1.1"><circle cx="6" cy="6" r="5"/><ellipse cx="6" cy="6" rx="2.2" ry="5"/><path d="M1 6 H11"/></svg>
        www.vantormedica.example
      </li>
    </ul>
  </section>

</div>
</body>
</html>
```